Varnek Group Business Card

Varnek Group — Business Card Design Brief
Overview
Design a double-sided business card for Varnek Group that highlights our two service arms: Varnek Communications (telecommunications) and Varnek Energy (business energy solutions). The card should feel smart and stand out when handed to clients.

Objectives
Showcase our areas of specialty clearly.
Reflect the overall Varnek / Varnek Group brand while acknowledging both arms.
Explore using both logos (Communications + Energy) or one unified logo, depending on the design.

Deliverables
One double-sided business card design (front + back).

Content & Copy
Front (preferred): Logo: Varnek / Varnek Group
Descriptor: Business Communications | Business Energy
Back:My contact details and company details
Core products: Business Mobile • Telephony • Internet • Business Energy Solutions

Brand & Visual Direction
We have a group logo currently tailored more toward telecoms, plus a separate Varnek Energy logo.
Please explore layouts that use both logos or just one, whichever works best.
Color: I wouldn't mind seeing an option using our the Blue/Purple gradient from our website (varnek-example.co.uk), but also open to non-gradient approaches and other colours..

Overall look: Smart, modern, and distinctive.
Format & Print Specs
Double-sided business card format. (Use a standard size

Must-Haves
Front: Varnek wording or Varnek Group wording with atleast 1 logo also on front “Business Communications | Business Energy.”

Back: Contact + company details and core products.
A design that stands out while remaining professional.

Nice-to-Have Options
A gradient version using our site’s Blue/Purple gradient.
A non-gradient version.
A dual-logo treatment versus a single-logo treatment.

Thanks
Dominic

```html
<!DOCTYPE html>
<html lang="en">
<head>
<meta charset="utf-8">
<title>Varnek Group Business Card</title>
<link href="https://fonts.googleapis.com/css2?family=Arimo:wght@400;700&display=swap" rel="stylesheet">
<style>
  :root {
    --page: #ebebeb;
    --white: #ffffff;
    --navy: #1b1464;
    --panel-blue: #0f5bd6;
    --band-green: #3aaa1a;
    --lime: #8cc63f;
    --energy-green: #6cb52d;
    --comms-blue: #1a7fd6;
    --logo-blue: #1565d8;
  }
  * { margin: 0; padding: 0; box-sizing: border-box; }
  html, body {
    width: 1200px; height: 1200px; overflow: hidden;
    background: var(--page);
    font-family: "Arimo", Arial, sans-serif;
  }
  .canvas { position: relative; width: 1200px; height: 1200px; }

  .card {
    position: absolute;
    width: 689px; height: 393px;
    background: var(--white);
    overflow: hidden;
  }
  .card--back { left: 267px; top: 159px; }
  .card--front { left: 262px; top: 653px; }

  /* contact side */
  .edge-stripe {
    position: absolute; left: 0; top: 0;
    width: 14px; height: 100%;
    background: var(--navy);
  }
  .brand-block {
    position: absolute; left: 14px; top: 0;
    width: 366px; height: 100%;
  }
  .brand-mark {
    position: absolute; left: 50%; transform: translateX(-50%);
    border-radius: 50%;
  }
  .brand-block .brand-mark {
    top: 107px; width: 120px; height: 120px;
    background: var(--energy-green);
  }
  .brand-name {
    position: absolute; left: 0; width: 100%;
    text-align: center;
    font-weight: 700; font-size: 58px; line-height: 1;
    color: var(--navy);
  }
  .brand-block .brand-name { top: 229px; }
  .brand-tagline {
    position: absolute; left: 0; width: 100%;
    text-align: center;
  }
  .brand-block .brand-tagline {
    top: 288px;
    font-size: 16px; letter-spacing: 3px;
    color: var(--energy-green);
  }

  .info-panel {
    position: absolute; left: 380px; top: 0;
    width: 309px; height: 100%;
    background: var(--panel-blue);
    color: var(--white);
  }
  .info-panel .line { position: absolute; left: 47px; white-space: nowrap; }
  .person-name {
    top: 38px; font-size: 27px; font-weight: 700;
    color: var(--lime); letter-spacing: 0.3px;
  }
  .person-title { top: 67px; font-size: 16px; }
  .address { top: 105px; font-size: 17px; line-height: 21px; }
  .contact { font-size: 17px; }
  .contact--phone { top: 158px; }
  .contact--mobile { top: 178px; }
  .contact--email { top: 199px; }
  .contact-icon {
    position: absolute; left: -26px; top: 2px;
    width: 14px; height: 16px;
  }
  .web-band {
    position: absolute; left: 0; top: 232px;
    width: 100%; height: 32px;
    background: var(--band-green);
  }
  .web-band .line { top: 7px; font-size: 16px; }
  .services {
    position: absolute; left: 47px; top: 276px;
    list-style: none;
    font-size: 18px; line-height: 21.5px;
  }
  .services li::before { content: "• "; font-size: 14px; vertical-align: 2px; }

  /* logo side */
  .card--front .brand-mark {
    top: 84px; width: 120px; height: 120px;
    background: var(--logo-blue);
  }
  .card--front .brand-name { top: 212px; }
  .card--front .brand-tagline {
    top: 281px; font-size: 17px;
    color: var(--comms-blue);
  }
</style>
</head>
<body>
<div class="canvas">

  <section class="card card--back" aria-label="Contact side">
    <div class="edge-stripe"></div>
    <div class="brand-block">
      <div class="brand-mark"></div>
      <div class="brand-name">VARNEK</div>
      <div class="brand-tagline">BUSINESS ENERGY</div>
    </div>

    <div class="info-panel">
      <div class="line person-name">ALAN REEVE</div>
      <div class="line person-title">President</div>
      <div class="line address">412 Birchwood Road<br>Halden, Canada 58210</div>

      <div class="line contact contact--phone">
        <svg class="contact-icon" viewBox="0 0 14 16" aria-hidden="true">
          <path d="M3 1 L5.5 1 L6.5 5 L4.8 6.2 C5.6 8.4 6.8 9.8 8.6 11 L10 9.4 L13 10.6 L13 13.4 C9 14.5 1.5 8 2.2 2 Z" fill="#8cc63f"/>
        </svg>555-210-4821
      </div>
      <div class="line contact contact--mobile">
        <svg class="contact-icon" viewBox="0 0 14 16" aria-hidden="true">
          <rect x="2.5" y="0.8" width="9" height="14.4" rx="1.5" fill="none" stroke="#8cc63f" stroke-width="1.8"/>
          <rect x="5.5" y="12" width="3" height="1.4" fill="#8cc63f"/>
        </svg>555-210-7396
      </div>
      <div class="line contact contact--email">
        <svg class="contact-icon" viewBox="0 0 14 16" aria-hidden="true">
          <rect x="0.5" y="4" width="13" height="9" fill="#8cc63f"/>
          <path d="M0.5 4 L7 9 L13.5 4" fill="none" stroke="#0f5bd6" stroke-width="1.2"/>
        </svg>info@varnek-example.com
      </div>

      <div class="web-band"><div class="line">www.varnek-example.com</div></div>

      <ul class="services">
        <li>Business Mobile</li>
        <li>Telephony</li>
        <li>Internet</li>
        <li>Business Energy Solutions</li>
      </ul>
    </div>
  </section>

  <section class="card card--front" aria-label="Logo side">
    <div class="brand-mark"></div>
    <div class="brand-name">VARNEK</div>
    <div class="brand-tagline">BUSINESS COMMUNICATIONS</div>
  </section>

</div>
</body>
</html>
```